Grins of Pellbrook - Dental, needs a redesign

Purpose:
Redesign website: http://www.grinsofpellbrook.example/

Sections are important, but for content, we can use existing website or have some placeholder text to fill in later.

Some of the required sections:
About us, contact us, services, our offices, our staff, patient education, patient forms (link to Molavex can be used here), link to friendspace, testimonials

Editability:
We would like to be able to update and edit the content in the future, for small changes

Pictures:
Here is a link to the staff pictures we’d like to use on the website:
https://www.filecrate.example/sh/493kq7zz2tt118p5/BBDRmwLe_uKPi8ZrafQWTGeeb?dl=0
You don't have to use all the pictures; just a few.

friendspace page:
https://www.friendspace.example/Grins-of-Pellbrook-627150384019562

Colors: Calming colors/images for a soothing feeling... to assure the patient that it'll not be that bad.

Target Market(s)

General population

Industry/Entity Type

Dental Clinic

Coding

Coded - Design and coding required

Number of Pages Required

5+ page

Requirements
Must have
• About us, contact us, services, our offices, our staff, patient education, patient forms (link to Molavex can be used here), link to friendspace, testimonials.
• Just create the placeholders for content or use from existing website.
• The staff picture of everyone needs to be on the home page - because that makes it more personal and has received positive feedback from many patients.

```html
<!DOCTYPE html>
<html lang="en">
<head>
<meta charset="utf-8">
<title>Grins of Pellbrook - Dental</title>
<link rel="stylesheet" href="https://fonts.googleapis.com/css2?family=Raleway:ital,wght@0,400;0,600;0,700;0,800;1,800&family=Lato:wght@400;700&display=swap">
<style>
:root{
  --teal:#3ec5c9;
  --teal-dark:#2aa9ae;
  --teal-deep:#1f8f94;
  --purple:#a57fe6;
  --purple-soft:#b597ee;
  --ink:#3a3a3a;
  --muted:#7a7a7a;
  --light:#f3f3f3;
  --footer:#262626;
  --footer-bar:#1a1a1a;
  --white:#ffffff;
}
*{box-sizing:border-box;margin:0;padding:0}
html,body{width:1200px;height:3046px;overflow:hidden}
body{font-family:"Lato",sans-serif;color:var(--ink);background:var(--white);position:relative}
.wrap{width:1000px;margin:0 auto;position:relative}

/* top bar */
.topbar{height:45px;background:var(--teal);}
.topbar .wrap{display:flex;justify-content:flex-end;align-items:center;height:45px;gap:26px;color:var(--white);font-size:14px;font-weight:700}
.topbar .item{display:flex;align-items:center;gap:8px}
.topbar .ico{width:20px;height:20px;border-radius:50%;background:var(--white);display:flex;align-items:center;justify-content:center}
.topbar .social{width:22px;height:22px;border-radius:50%;background:var(--white);opacity:.9}

/* nav */
.header{height:93px;background:var(--white);border-bottom:1px solid #e6e6e6}
.header .wrap{display:flex;align-items:center;justify-content:space-between;height:93px}
.brand{display:flex;align-items:center;gap:12px;font-family:"Raleway",sans-serif;font-weight:700;font-size:30px;color:var(--purple);letter-spacing:.5px}
.brand .dot{width:34px;height:34px;border-radius:50%;background:var(--teal)}
.nav{display:flex;gap:0;font-size:14px}
.nav a{color:var(--ink);text-decoration:none;padding:0 13px;border-left:1px solid #d8d8d8}
.nav a:first-child{border-left:none;color:var(--purple);text-decoration:underline}

/* hero */
.hero{height:512px;position:relative;background:linear-gradient(100deg,#e9e4e0 0%,#d9cfc9 35%,#f2f0ee 60%,#e8eaec 100%)}
.hero .arrow{position:absolute;top:230px;color:#fff;font-size:30px;opacity:.8}
.hero .arrow.l{left:18px}.hero .arrow.r{right:18px}
.hero-band{position:absolute;left:0;right:0;bottom:0;height:86px;background:rgba(40,40,40,.78)}
.hero-band .wrap{display:flex;align-items:center;justify-content:space-between;height:86px}
.hero-band h1{font-family:"Raleway",sans-serif;font-style:italic;font-weight:800;font-size:33px;color:var(--white)}
.btn-appt{display:flex;align-items:center;gap:14px;background:var(--teal);color:var(--white);font-family:"Raleway",sans-serif;font-weight:700;font-size:18px;padding:10px 22px 10px 10px;margin-right:-20px}
.btn-appt .cal{width:32px;height:32px;border:2px solid #fff;border-radius:3px;display:flex;align-items:flex-end;justify-content:center;font-size:11px;padding-bottom:2px}

/* headings */
.sec-title{text-align:center;font-family:"Raleway",sans-serif;font-weight:700;font-size:31px;letter-spacing:.5px}
.divider{display:flex;align-items:center;justify-content:center;gap:0;margin:10px auto 0;width:240px;position:relative;height:20px}
.divider::before{content:"";position:absolute;left:0;right:0;top:9px;height:1px;background:currentColor;opacity:.35}
.divider span{width:14px;height:14px;border-radius:50%;background:currentColor;position:relative}

/* welcome */
.welcome{height:330px;padding-top:26px}
.welcome .sec-title{color:var(--purple)}
.welcome .sec-title b{color:var(--teal);font-weight:700}
.welcome .divider{color:var(--purple)}
.welcome p{width:960px;margin:22px auto 0;text-align:center;font-size:13.4px;line-height:27px;color:#555}
.btn-small{display:block;width:104px;margin:18px auto 0;background:var(--teal);color:#fff;font-size:13px;font-weight:700;text-align:center;padding:10px 0}

/* services */
.services{height:528px;background:linear-gradient(160deg,#55cfd1 0%,#3ec0c4 55%,#2fb1b6 100%);color:var(--white);padding-top:40px}
.services .divider{color:#fff}
.svc-grid{position:relative;height:380px;margin-top:20px}
.svc{position:absolute;width:350px;display:flex;gap:20px;align-items:center}
.svc .txt h3{font-family:"Raleway",sans-serif;font-weight:700;font-size:20px}
.svc .txt p{font-size:13px;line-height:17px;color:rgba(255,255,255,.85);margin-top:4px}
.svc .box{flex:none;width:96px;height:96px;border:3px solid var(--teal-deep);border-radius:6px;display:flex;align-items:center;justify-content:center}
.svc.left{left:30px;flex-direction:row}
.svc.left .txt{text-align:right}
.svc.right{right:30px}
.svc.r1{top:40px}.svc.r2{top:206px}
.center-mark{position:absolute;left:50%;top:0;transform:translateX(-50%);width:220px;height:280px;display:flex;flex-direction:column;align-items:center;justify-content:center;gap:14px}
.center-mark .ring{width:200px;height:200px;border-radius:50%;border:5px solid rgba(255,255,255,.85)}
.center-mark .name{font-family:"Raleway",sans-serif;font-weight:700;font-size:20px;color:var(--white)}

/* team */
.team{height:432px;background:var(--light);padding-top:26px}
.team .sec-title{color:var(--purple)}
.team .divider{color:var(--purple)}
.team-row{display:flex;gap:9px;justify-content:center;margin-top:20px}
.member{width:194px;background:var(--white)}
.member .photo{height:130px;background:linear-gradient(180deg,#a3644b 0%,#8c5a47 55%,#3d3333 100%)}
.member .photo.b{background:linear-gradient(180deg,#b9c0c8 0%,#8b8f94 55%,#2e2e30 100%)}
.member .body{padding:12px 14px 14px}
.member h4{color:var(--teal);font-size:14px;font-weight:700}
.member p{font-size:12.5px;line-height:17px;color:#777;margin-top:6px}
.member p em{color:var(--teal);font-style:normal}

/* hours & testimonials */
.split{height:450px;display:flex}
.hours{width:600px;background:linear-gradient(135deg,#5dd0d2 0%,#3fb9bd 100%);color:#fff;padding-top:30px}
.hours .divider,.testi .divider{color:#fff;width:240px}
.hours .sec-title,.testi .sec-title{font-size:30px}
.hours-table{margin:40px 0 0 70px;width:470px}
.hours-row{display:flex;align-items:center;height:46px;font-family:"Raleway",sans-serif;font-weight:700;background:linear-gradient(90deg,rgba(255,255,255,0) 0%,rgba(255,255,255,.18) 30%,rgba(255,255,255,.18) 70%,rgba(255,255,255,0) 100%);margin-bottom:2px}
.hours-row .day{width:165px;text-align:right;font-size:15px}
.hours-row .day small{display:block;font-size:13px;line-height:13px}
.hours-row .sep{width:40px;text-align:center}
.hours-row .time{font-size:18px;line-height:24px}
.testi{flex:1;background:linear-gradient(135deg,#b596ee 0%,#a07de3 100%);color:#fff;padding-top:30px;text-align:center}
.avatars{display:flex;justify-content:center;align-items:center;margin-top:34px;position:relative}
.avatars .av{border-radius:50%;border:3px solid #fff;margin:0 -6px;background:linear-gradient(180deg,#d8c8c0,#8f7a86)}
.avatars .s{width:56px;height:56px;opacity:.8}
.avatars .m{width:70px;height:70px;opacity:.9}
.avatars .l{width:110px;height:110px;position:relative;z-index:2}
.avatars .nav-a{position:absolute;top:36px;font-size:28px;opacity:.9}
.avatars .nav-a.l{left:30px;width:auto;height:auto}.avatars .nav-a.r{right:30px}
.testi h4{font-family:"Raleway",sans-serif;font-weight:700;font-size:24px;margin-top:20px}
.testi p{width:430px;margin:20px auto 0;font-size:13px;line-height:20px}

/* appointment */
.appt{height:310px;position:relative;background:var(--white);overflow:hidden}
.appt .intro{position:absolute;left:100px;top:48px;width:320px}
.appt h2{font-family:"Raleway",sans-serif;font-weight:700;font-size:36px;line-height:46px;color:var(--teal)}
.appt .intro p{font-size:13px;line-height:20px;color:#666;margin-top:18px}
.appt .form{position:absolute;left:458px;top:48px;width:642px}
.appt .form label{font-size:13px;color:#555}
.fields{display:grid;grid-template-columns:1fr 1fr;gap:10px 20px;margin-top:14px}
.fields div{height:44px;border:1px solid #d7d7d7;font-size:13px;color:#777;padding:13px 14px}
.appt .submit{display:inline-block;margin-top:12px;background:var(--teal);color:#fff;font-size:15px;padding:11px 14px}
.appt svg.wave{position:absolute;left:0;bottom:0}

/* footer */
.footer{height:305px;background:var(--footer);color:#ddd}
.footer .wrap{display:flex;padding-top:42px;height:305px}
.fcol h5{font-family:"Raleway",sans-serif;color:var(--teal);font-size:18px;font-weight:700;padding-bottom:6px;border-bottom:1px solid #444;display:inline-block}
.fcol ul{list-style:none;margin-top:10px}
.fcol.links{width:195px;padding-left:22px}
.fcol.links li{font-size:13.5px;line-height:23px}
.fcol.links li::before{content:"›";color:var(--teal);margin-right:7px}
.fcol.contact{width:282px}
.fcol.contact li{display:flex;gap:10px;font-size:13.5px;line-height:20px;margin-bottom:10px}
.fcol.contact .ic{color:var(--teal);width:14px;flex:none}
.fcol.news{width:260px}
.fcol.news p{font-size:13.5px;line-height:20px;margin-top:10px}
.fcol.news .email{margin-top:28px;width:190px;height:30px;background:#fff;color:#777;font-size:13px;padding:7px 10px}
.fcol.news .sub{margin-top:12px;display:inline-block;background:var(--teal);color:#fff;font-size:13px;font-weight:700;padding:7px 10px}
.fbrand{flex:1;display:flex;flex-direction:column;align-items:center;justify-content:center;padding-bottom:40px;gap:14px}
.fbrand .dot{width:60px;height:60px;border-radius:50%;background:var(--teal-deep)}
.fbrand .name{font-family:"Raleway",sans-serif;font-weight:700;font-size:24px;color:var(--teal-deep);text-align:center;line-height:28px}
.bottombar{height:41px;background:var(--footer-bar);color:#ddd;font-size:13px}
.bottombar .wrap{display:flex;justify-content:space-between;align-items:center;height:41px;padding-left:20px}
.bottombar .follow{display:flex;align-items:center;gap:10px;font-weight:700}
.bottombar .follow span{width:26px;height:26px;border-radius:50%;border:2px solid #ddd}
</style>
</head>
<body>

<div class="topbar">
  <div class="wrap">
    <div class="item"><span class="ico"><svg width="11" height="11" viewBox="0 0 24 24"><path fill="#3ec5c9" d="M6.6 10.8a15 15 0 0 0 6.6 6.6l2.2-2.2a1 1 0 0 1 1-.25 11.4 11.4 0 0 0 3.6.57 1 1 0 0 1 1 1V20a1 1 0 0 1-1 1A17 17 0 0 1 3 4a1 1 0 0 1 1-1h3.5a1 1 0 0 1 1 1c0 1.25.2 2.45.57 3.6a1 1 0 0 1-.25 1z"/></svg></span>555-018-2461</div>
    <div class="item"><span class="ico"><svg width="11" height="11" viewBox="0 0 24 24"><path fill="#3ec5c9" d="M2 5h20v14H2z M2 5l10 8 10-8" stroke="#fff" stroke-width="1.5"/></svg></span>info@grinsofpellbrook.example</div>
    <span class="social" aria-label="friendspace"></span>
  </div>
</div>

<header class="header">
  <div class="wrap">
    <div class="brand"><span class="dot"></span>Grins of Pellbrook</div>
    <nav class="nav">
      <a>Home</a><a>About us</a><a>Services</a><a>Our Staff</a><a>Testimonials</a><a>Our offices</a><a>Contact us</a>
    </nav>
  </div>
</header>

<section class="hero" role="img" aria-label="Dentist examining a smiling patient with braces">
  <span class="arrow l">‹</span><span class="arrow r">›</span>
  <div class="hero-band">
    <div class="wrap">
      <h1>Honestly Caring &amp; Quality Dentistry</h1>
      <div class="btn-appt"><span class="cal">31</span>MAKE AN APPOINTMENT</div>
    </div>
  </div>
</section>

<section class="welcome">
  <h2 class="sec-title">WELCOME TO <b>GRINS OF PELLBROOK</b></h2>
  <div class="divider"><span></span></div>
  <p>Dr. Meera Castell provides a full range of dental services to the whole family. Many of our patient families span multiple generations. Our Team are dedicated to taking the time needed to provide the very best care every patient deserves. Please tour our web site to learn more about family dentistry, cosmetic dentistry and our restorative dental services. We invite you to call us with any questions you may have - we all look forward to meeting you and your family! New patients looking for quality dental care in a relaxed environment are welcome! We accept PPO, Indeminity and Traditional Insurance plans.</p>
  <span class="btn-small">READ MORE</span>
</section>

<section class="services">
  <h2 class="sec-title">OUR SERVICES</h2>
  <div class="divider"><span></span></div>
  <div class="wrap svc-grid">
    <div class="svc left r1"><div class="txt"><h3>General Dental Health</h3><p>Ut wisi enim ad minim veniam, quismpi [+]... nostrud exerci tation ullamco</p></div><div class="box"><svg width="44" height="44" viewBox="0 0 44 44" fill="none" stroke="#fff" stroke-width="3"><path d="M14 6v22M30 6v22"/><rect x="10" y="28" width="8" height="10" rx="2"/><rect x="26" y="28" width="8" height="10" rx="2"/></svg></div></div>
    <div class="svc left r2"><div class="txt"><h3>Dental FAQ</h3><p>Ut wisi enim ad minim veniam, quismpi [+]... nostrud exerci tation ullamco</p></div><div class="box"><svg width="44" height="44" viewBox="0 0 44 44" fill="none" stroke="#fff" stroke-width="3"><circle cx="22" cy="22" r="16"/><path d="M22 30v1M17 17a5 5 0 1 1 5 6v3"/></svg></div></div>
    <div class="center-mark" aria-label="Grins of Pellbrook"><span class="ring"></span><span class="name">Grins of Pellbrook</span></div>
    <div class="svc right r1"><div class="box"><svg width="48" height="30" viewBox="0 0 48 30" fill="none" stroke="#fff" stroke-width="3"><path d="M3 6c12 6 30 6 42 0c-4 14-14 20-21 20S7 20 3 6z"/></svg></div><div class="txt"><h3>Cosmetic Dentistry</h3><p>Ut wisi enim ad minim veniam, quismpi nostrud exerci tation ullamco ...[+]</p></div></div>
    <div class="svc right r2"><div class="box"><svg width="44" height="44" viewBox="0 0 44 44" fill="none" stroke="#fff" stroke-width="3"><path d="M8 36h28M14 36V22h20M14 22l-4-10"/><circle cx="30" cy="12" r="4"/></svg></div><div class="txt"><h3>Advanced Procedures</h3><p>Ut wisi enim ad minim veniam, quismpi nostrud exerci tation ullamco ...[+]</p></div></div>
  </div>
</section>

<section class="team">
  <h2 class="sec-title">OUR TEAM</h2>
  <div class="divider"><span></span></div>
  <div class="team-row">
    <div class="member"><div class="photo" role="img" aria-label="Portrait of Dr. Meera Castell"></div><div class="body"><h4>Dr. Meera Castell</h4><p>Duis autem vel eum iriure dolormi opl innokl hendi rerit vulpu tatemi velitm <em>[+]</em></p></div></div>
    <div class="member"><div class="photo b" role="img" aria-label="Portrait of a team member"></div><div class="body"><h4>Lorem ipsum</h4><p>Duis autem vel eum iriure dolormi opl innokl hendi rerit vulpu tatemi velitm <em>[+]</em></p></div></div>
    <div class="member"><div class="photo" role="img" aria-label="Portrait of a team member"></div><div class="body"><h4>Lorem ipsum</h4><p>Duis autem vel eum iriure dolormi opl innokl hendi rerit vulpu tatemi velitm <em>[+]</em></p></div></div>
    <div class="member"><div class="photo" role="img" aria-label="Portrait of a team member"></div><div class="body"><h4>Lorem ipsum</h4><p>Duis autem vel eum iriure dolormi opl innokl hendi rerit vulpu tatemi velitm <em>[+]</em></p></div></div>
    <div class="member"><div class="photo b" role="img" aria-label="Portrait of a team member"></div><div class="body"><h4>Lorem ipsum</h4><p>Duis autem vel eum iriure dolormi opl innokl hendi rerit vulpu tatemi velitm <em>[+]</em></p></div></div>
  </div>
</section>

<section class="split">
  <div class="hours" role="img" aria-label="Softly blurred clinic interior in teal tones">
    <h2 class="sec-title">OPENING HOURS</h2>
    <div class="divider"><span></span></div>
    <div class="hours-table">
      <div class="hours-row"><span class="day">Monday</span><span class="sep">:</span><span class="time">12:00pm to 6:00pm</span></div>
      <div class="hours-row"><span class="day">Tuesday</span><span class="sep">:</span><span class="time">10:00am to 7:00pm</span></div>
      <div class="hours-row"><span class="day">Wednesday</span><span class="sep">:</span><span class="time">Closed</span></div>
      <div class="hours-row"><span class="day">Friday</span><span class="sep">:</span><span class="time">8:00am to 6:00pm</span></div>
      <div class="hours-row" style="height:64px"><span class="day">Saturday<small>when open</small></span><span class="sep">:</span><span class="time">8:00am to 3:00pm OR<br>8:00am to 12:00pm</span></div>
    </div>
  </div>
  <div class="testi">
    <h2 class="sec-title">TESTIMONIALS</h2>
    <div class="divider"><span></span></div>
    <div class="avatars">
      <span class="nav-a l">‹</span>
      <span class="av s" role="img" aria-label="Patient portrait"></span>
      <span class="av m" role="img" aria-label="Patient portrait"></span>
      <span class="av l" role="img" aria-label="Portrait of John Doe"></span>
      <span class="av m" role="img" aria-label="Patient portrait"></span>
      <span class="av s" role="img" aria-label="Patient portrait"></span>
      <span class="nav-a r">›</span>
    </div>
    <h4>-John Doe</h4>
    <p>Ut wisi enim adi minim veniam, quis nostrudk exerci tation more ullamcorper suscipit lobortis nis ut aliquip commodo consequ. quis nostrudk Ut wisi enim aliquip adi minim veniam</p>
  </div>
</section>

<section class="appt">
  <div class="intro">
    <h2>MAKE AN<br>APPOINTMENT</h2>
    <p>Duis autem vel eum iriure dolormi opl innokl hendi rerit in vulpu tatemi velitm essemol mo molestiel conseqh uat, velmi illum dolor eokf no atn nulla more facilisis</p>
  </div>
  <div class="form">
    <label>Please fill up bellow form</label>
    <div class="fields"><div>Name</div><div>Email</div><div>Phone</div><div>Message</div></div>
    <span class="submit">SUBMIT</span>
  </div>
  <svg class="wave" width="1200" height="150" viewBox="0 0 1200 150" aria-hidden="true">
    <path d="M0 20 C250 130 650 60 1200 10 L1200 150 L0 150 Z" fill="#2aa9ae"/>
    <path d="M0 45 C260 150 660 90 1200 40 L1200 150 L0 150 Z" fill="#262626"/>
  </svg>
</section>

<footer class="footer">
  <div class="wrap">
    <div class="fcol links"><h5>Quick Links</h5>
      <ul><li>Home</li><li>About Us</li><li>Services</li><li>Our Staff</li><li>Testimonials</li><li>Our offices</li><li>Contact us</li></ul>
    </div>
    <div class="fcol contact"><h5>Contact Details</h5>
      <ul>
        <li><span class="ic">●</span><span>418 W. Harrow Lane,<br>Suite 2C Pellbrook,<br>ZZ 00417</span></li>
        <li><span class="ic">✆</span><span>555-018-2461<br>555-018-2463</span></li>
        <li><span class="ic">✉</span><span>info@grinsofpellbrook.example</span></li>
      </ul>
    </div>
    <div class="fcol news"><h5>Newsletter Sign Up</h5>
      <p>Ut wisi enim ad minim veniam nk quis nostrud exerci tationmo ullm amcorper suscipit lobortis nisl.</p>
      <div class="email">Email Address</div>
      <span class="sub">Subscribe</span>
    </div>
    <div class="fbrand"><span class="dot"></span><span class="name">Grins of Pellbrook</span></div>
  </div>
</footer>
<div class="bottombar">
  <div class="wrap">
    <span>Copyright © 2016 GRINS OF PELLBROOK. All Right Reserved.</span>
    <span class="follow">Follow Us On <span aria-label="friendspace"></span></span>
  </div>
</div>

</body>
</html>
```